Creative Businesss Card desgin!

Create a business card for our business Glint window cleaning!
We are open to creative ideas as long as it maintains a professional image.

Target Market(s)

Small Commercial window cleaning clients including car dealerships, strata manager, cafe

Industry/Entity Type

Window Cleaning

Contact Information for Business Card

Darren Pilkey
General Manager
Glint Window Cleaning

darren@glintservices.com.au
pane-tidy-corner.com.au
Ph: 1800 GO GLINT
Mob: 0438 572 619

Colors
fbed22
0392cd

Requirements
Should not have
• Stock window cleaning/ squeegee graphics

```html
<!DOCTYPE html>
<html lang="en">
<head>
<meta charset="utf-8">
<title>Glint Window Cleaning – Business Card</title>
<link rel="stylesheet" href="https://fonts.googleapis.com/css2?family=Roboto:wght@400;500;700&display=swap">
<style>
  :root {
    --backdrop: #2b2b2b;
    --brand-blue: #0f5584;
    --brand-yellow: #f4ef22;
    --faint-band: #25677f;
    --ink-blue: #0f4f80;
    --white: #ffffff;
  }
  * { margin: 0; padding: 0; box-sizing: border-box; }
  html, body {
    width: 1200px; height: 960px; overflow: hidden;
    background: var(--backdrop);
    font-family: "Roboto", Arial, sans-serif;
  }
  .canvas { position: relative; width: 1200px; height: 960px; }
  .card {
    position: absolute; width: 598px; height: 342px;
    background: var(--brand-blue); overflow: hidden;
    box-shadow: 0 3px 8px rgba(0,0,0,.45);
  }
  .card--front { left: 322px; top: 108px; }
  .card--back { left: 320px; top: 493px; }
  .card__shapes { position: absolute; inset: 0; width: 100%; height: 100%; }

  .contact { position: absolute; left: 33px; top: 30px; color: var(--ink-blue); }
  .contact__name { font-size: 21px; font-weight: 700; line-height: 1; letter-spacing: .2px; }
  .contact__title { font-size: 14px; font-weight: 500; margin-top: 4px; }
  .contact__company { font-size: 14px; margin-top: 24px; }
  .contact__lines { list-style: none; font-size: 14px; line-height: 18px; margin-top: 10px; }

  .wordmark {
    position: absolute; color: var(--brand-yellow);
    font-weight: 700; text-align: center; line-height: 1;
  }
  .wordmark__name { display: block; }
  .wordmark__tag { display: block; }
  .card--front .wordmark { right: 32px; bottom: 28px; }
  .card--front .wordmark__name { font-size: 62px; letter-spacing: 4px; }
  .card--front .wordmark__tag { font-size: 20px; margin-top: 6px; }
  .card--back .wordmark { right: 38px; top: 160px; }
  .card--back .wordmark__name { font-size: 92px; letter-spacing: 6px; }
  .card--back .wordmark__tag { font-size: 31px; margin-top: 8px; }

  .card__web {
    position: absolute; right: 32px; bottom: 30px;
    color: var(--white); font-size: 14.5px; letter-spacing: 1.2px;
  }
</style>
</head>
<body>
<main class="canvas">
  <section class="card card--front" aria-label="Card front">
    <svg class="card__shapes" viewBox="0 0 598 342" aria-hidden="true">
      <polygon points="0,0 330,0 190,342 0,342" fill="var(--brand-yellow)"/>
      <line x1="340" y1="0" x2="200" y2="342" stroke="var(--brand-yellow)" stroke-width="3"/>
    </svg>
    <div class="contact">
      <p class="contact__name">DARREN PILKEY</p>
      <p class="contact__title">GENERAL MANAGER</p>
      <p class="contact__company">Glint Window Cleaning</p>
      <ul class="contact__lines">
        <li>(P) 1800 GO GLINT</li>
        <li>(M) 0438 572 619</li>
        <li>darren@glintservices.com.au</li>
        <li>pane-tidy-corner.com.au</li>
      </ul>
    </div>
    <p class="wordmark">
      <span class="wordmark__name">GLINT</span>
      <span class="wordmark__tag">WINDOW CLEANING</span>
    </p>
  </section>

  <section class="card card--back" aria-label="Card back">
    <svg class="card__shapes" viewBox="0 0 598 342" aria-hidden="true">
      <polygon points="120,0 200,0 80,342 0,342 0,180" fill="var(--faint-band)"/>
    </svg>
    <p class="wordmark">
      <span class="wordmark__name">GLINT</span>
      <span class="wordmark__tag">WINDOW CLEANING</span>
    </p>
    <p class="card__web">www.pane-tidy-corner.com.au</p>
  </section>
</main>
</body>
</html>
```